Dance Card to Provide Contact Info

I'm looking for a double sided business card to provide contact information to perspective dance partners.
One side of the card would have the words: "Yes I would love to Dance" written in an interesting and eye catching way. Below that would be the three categories I'm interested in
>Social >Exhibition >Competition
The other side of the card would include a picture of me with my Name, Phone Number, and Email Address (Dale Pruitt, 210-574-1328, dale@twirlnstep.dance)
My target market is middle aged women interested in Country and Western dancing and West Coast Swing dancing. I am NOT particularly interested in Ballroom style.
Here are a few links to the type of dancing I want to do:
http://www.plvkrn.org/
http://www.prairiefolkstepsociety.com/
http://mesquitevalleytwostep.com/
Dale Pruitt
210-574-1328
dale@twirlnstep.dance

```html
<!DOCTYPE html>
<html lang="en">
<head>
<meta charset="utf-8">
<title>Yes! I Would Love to Dance – Dance Card</title>
<link rel="stylesheet" href="https://fonts.googleapis.com/css2?family=Permanent+Marker&display=swap">
<style>
  :root {
    --card-bg: #111111;
    --card-bg-light: #1c1c1c;
    --ink-blue: #2d6fd2;
    --ink-red: #c93b3b;
    --ink-outline: #ffffff;
    --brush-font: "Permanent Marker", cursive;
  }
  * { margin: 0; padding: 0; box-sizing: border-box; }
  html, body {
    width: 1200px;
    height: 667px;
    overflow: hidden;
    background: var(--card-bg);
  }
  .dance-card {
    position: relative;
    width: 1200px;
    height: 667px;
    overflow: hidden;
    font-family: var(--brush-font);
    text-transform: uppercase;
  }
  .damask-backdrop {
    position: absolute;
    inset: 0;
    background: radial-gradient(ellipse at center, var(--card-bg-light) 0%, var(--card-bg) 75%);
  }
  .headline {
    position: absolute;
    left: 0;
    right: 0;
    text-align: center;
    line-height: 1;
    font-style: italic;
    text-shadow:
      -2px -2px 0 var(--ink-outline), 2px -2px 0 var(--ink-outline),
      -2px 2px 0 var(--ink-outline), 2px 2px 0 var(--ink-outline),
      0 -2px 0 var(--ink-outline), 0 2px 0 var(--ink-outline),
      -2px 0 0 var(--ink-outline), 2px 0 0 var(--ink-outline);
  }
  .headline--yes {
    top: 118px;
    font-size: 118px;
    color: var(--ink-blue);
    letter-spacing: 2px;
  }
  .headline--love {
    top: 232px;
    font-size: 86px;
    color: var(--ink-red);
    letter-spacing: 1px;
  }
  .headline--dance {
    top: 346px;
    font-size: 132px;
    color: var(--ink-blue);
    letter-spacing: 1px;
  }
  .categories {
    position: absolute;
    left: 0;
    right: 0;
    top: 594px;
    text-align: center;
    font-size: 36px;
    line-height: 1;
    font-style: italic;
    letter-spacing: 1px;
    text-shadow:
      -1.5px -1.5px 0 var(--ink-outline), 1.5px -1.5px 0 var(--ink-outline),
      -1.5px 1.5px 0 var(--ink-outline), 1.5px 1.5px 0 var(--ink-outline);
  }
  .categories__item--red { color: var(--ink-red); }
  .categories__item--blue { color: var(--ink-blue); }
  .categories__divider { color: var(--ink-blue); padding: 0 6px; }
</style>
</head>
<body>
  <main class="dance-card">
    <div class="damask-backdrop" role="img" aria-label="Dark black damask wallpaper pattern background"></div>

    <h1 class="headline headline--yes">Yes!</h1>
    <p class="headline headline--love">I Would Love To</p>
    <p class="headline headline--dance">Dance!</p>

    <p class="categories">
      <span class="categories__item categories__item--red">Social</span><span class="categories__divider">/</span><span class="categories__item categories__item--blue">Exhibition</span><span class="categories__divider">/</span><span class="categories__item categories__item--red">Competition</span>
    </p>
  </main>
</body>
</html>
```